Bref créative
Quillmont Care Associates
Business Cards & Stationary
Bright & Fun-filled
Harold J. Mabbery, Ph.D.
Co-founder
4815 North Larkin Road
Vista, CA 92083
drhmabbery@examplemail.net
Licensed Psychologist PSY58706
On the front of the card, we would like to see some versions with the logos symbol.
This business card is for a California Board Licensed Psychologist.
The look of this should be professional, but because it is for therapy, we would like it to be professional with a hint of:
* warm and welcoming
* serenity, tranquility and happiness
* positive, future, growth
On the back of the business card please place the:
1. Logo symbol and company name
2. Child, Adolescence, Family, Adult Therapy
logo
We need to see how the back of a card looks with the Quillmont Care Logo and the following information attached.

```html
<!DOCTYPE html>
<html lang="en">
<head>
<meta charset="utf-8">
<title>Quillmont Care Associates — Stationery Concepts</title>
<link href="https://fonts.googleapis.com/css2?family=Cinzel:wght@600&family=Open+Sans:wght@400;600&display=swap" rel="stylesheet">
<style>
:root{
  --backdrop:#efe7dc;
  --paper:#ffffff;
  --blue:#2f8fd0;
  --teal:#8fd3e0;
  --teal-soft:#cdeef3;
  --navy:#1f3b66;
  --muted:#6f7f92;
  --label:#7a6a58;
  --faint:#e6f1f8;
}
*{box-sizing:border-box;margin:0;padding:0}
html,body{width:1200px;height:446px;overflow:hidden;background:var(--backdrop)}
body{position:relative;font-family:"Open Sans",sans-serif;color:var(--navy)}
.piece{position:absolute;background:var(--paper);box-shadow:0 1px 3px rgba(0,0,0,.18);overflow:hidden}
.label{position:absolute;font-family:"Cinzel",serif;font-size:7px;letter-spacing:.08em;color:var(--label);text-transform:uppercase}
.brand{display:flex;align-items:center;gap:4px}
.brand-dot{border-radius:50%;background:var(--blue);flex:none}
.brand-name{font-family:"Cinzel",serif;font-weight:600;color:var(--navy);line-height:1.05}
.wave{position:absolute;left:0;bottom:0;width:100%}
.contact{font-size:4.5px;line-height:1.5;color:var(--muted);text-align:right}
.faint-circle{position:absolute;border-radius:50%;border:10px solid var(--faint)}
.footer-line{position:absolute;left:0;right:0;text-align:center;font-size:4.5px;color:var(--muted)}
</style>
</head>
<body>

<div class="label" style="left:12px;top:122px">Stationary Concepts</div>

<!-- Business card front -->
<div class="piece business-card" style="left:14px;top:180px;width:123px;height:62px">
  <div class="brand" style="position:absolute;left:7px;top:14px">
    <span class="brand-dot" style="width:9px;height:9px"></span>
    <span class="brand-name" style="font-size:5px">Quillmont<br>Care Associates</span>
  </div>
  <div class="contact" style="position:absolute;right:7px;top:10px">
    <strong style="color:var(--navy)">Harold J. Mabbery, Ph.D.</strong><br>Co-founder<br>4815 North Larkin Road<br>Vista, CA 92083<br>drhmabbery@examplemail.net<br>Licensed Psychologist PSY58706
  </div>
  <svg class="wave" viewBox="0 0 123 12" height="12" preserveAspectRatio="none"><path d="M0 6 Q40 0 70 6 T123 4 V12 H0Z" fill="var(--teal)"/><path d="M0 9 Q50 3 90 8 T123 7 V12 H0Z" fill="var(--blue)"/></svg>
</div>
<div class="label" style="left:20px;top:247px">Business Card Front</div>

<!-- Business card back -->
<div class="piece business-card" style="left:14px;top:260px;width:123px;height:62px">
  <div class="brand" style="position:absolute;left:7px;top:14px">
    <span class="brand-dot" style="width:9px;height:9px"></span>
    <span class="brand-name" style="font-size:5px">Quillmont<br>Care Associates</span>
  </div>
  <div class="contact" style="position:absolute;right:7px;top:26px;font-size:4px">Child, Adolescence, Family, Adult Therapy</div>
  <svg class="wave" viewBox="0 0 123 12" height="12" preserveAspectRatio="none"><path d="M0 6 Q40 0 70 6 T123 4 V12 H0Z" fill="var(--teal)"/><path d="M0 9 Q50 3 90 8 T123 7 V12 H0Z" fill="var(--blue)"/></svg>
</div>
<div class="label" style="left:20px;top:327px">Business Card Back</div>

<!-- Letterhead option 1 -->
<div class="piece letterhead" style="left:163px;top:19px;width:281px;height:365px">
  <div class="brand" style="position:absolute;left:22px;top:22px">
    <span class="brand-dot" style="width:14px;height:14px"></span>
    <span class="brand-name" style="font-size:7px">Quillmont<br>Care Associates</span>
  </div>
  <div class="contact" style="position:absolute;right:24px;top:22px">
    Harold J. Mabbery, Ph.D.<br>4815 North Larkin Road<br>Vista, CA 92083<br>drhmabbery@examplemail.net<br>PSY58706
  </div>
  <div class="faint-circle" style="left:160px;top:210px;width:100px;height:100px"></div>
  <svg class="wave" viewBox="0 0 281 40" height="40" preserveAspectRatio="none"><path d="M0 20 Q90 4 170 20 T281 14 V40 H0Z" fill="var(--teal-soft)"/><path d="M0 28 Q100 12 190 26 T281 22 V40 H0Z" fill="var(--teal)"/><path d="M0 34 Q120 22 210 33 T281 30 V40 H0Z" fill="var(--blue)"/></svg>
</div>
<div class="label" style="left:262px;top:391px">Letter Head Option 1</div>

<!-- Letterhead option 2 -->
<div class="piece letterhead" style="left:475px;top:19px;width:281px;height:365px">
  <div class="brand" style="position:absolute;left:22px;top:22px">
    <span class="brand-dot" style="width:14px;height:14px"></span>
    <span class="brand-name" style="font-size:7px">Quillmont<br>Care Associates</span>
  </div>
  <div class="faint-circle" style="left:95px;top:130px;width:120px;height:120px"></div>
  <div class="footer-line" style="bottom:44px">4815 North Larkin Road, Vista, CA 92083 &nbsp;|&nbsp; drhmabbery@examplemail.net &nbsp;|&nbsp; PSY58706</div>
  <svg class="wave" viewBox="0 0 281 40" height="40" preserveAspectRatio="none"><path d="M0 20 Q90 4 170 20 T281 14 V40 H0Z" fill="var(--teal-soft)"/><path d="M0 28 Q100 12 190 26 T281 22 V40 H0Z" fill="var(--teal)"/><path d="M0 34 Q120 22 210 33 T281 30 V40 H0Z" fill="var(--blue)"/></svg>
</div>
<div class="label" style="left:575px;top:391px">Letter Head Option 2</div>

<!-- Envelope back, blue -->
<div class="piece envelope" style="left:792px;top:19px;width:398px;height:96px;background:var(--blue)">
  <svg viewBox="0 0 398 96" width="398" height="96" style="position:absolute;left:0;top:0"><path d="M0 0 L199 38 L398 0" fill="none" stroke="#ffffff" stroke-opacity=".35" stroke-width="1"/><circle cx="199" cy="62" r="8" fill="#ffffff"/></svg>
</div>

<!-- Envelope back, teal -->
<div class="piece envelope" style="left:792px;top:96px;width:398px;height:96px;background:var(--teal)">
  <svg viewBox="0 0 398 96" width="398" height="96" style="position:absolute;left:0;top:0"><path d="M0 0 L199 44 L398 0" fill="var(--teal-soft)" stroke="#ffffff" stroke-width="1.5"/><circle cx="199" cy="68" r="7" fill="#ffffff"/></svg>
</div>

<!-- Envelope back, white -->
<div class="piece envelope" style="left:792px;top:170px;width:398px;height:110px">
  <svg viewBox="0 0 398 110" width="398" height="110" style="position:absolute;left:0;top:0"><path d="M0 0 L199 46 L398 0" fill="none" stroke="#d5dde4" stroke-width="1"/><path d="M0 110 L170 56 M398 110 L228 56" stroke="#e4e9ee" stroke-width="1"/><circle cx="199" cy="72" r="7" fill="var(--blue)"/></svg>
</div>

<!-- Envelope front -->
<div class="piece envelope" style="left:798px;top:290px;width:390px;height:94px">
  <div class="brand" style="position:absolute;left:16px;top:14px">
    <span class="brand-dot" style="width:12px;height:12px"></span>
    <span class="brand-name" style="font-size:6.5px">Quillmont<br>Care Associates</span>
  </div>
  <svg class="wave" viewBox="0 0 390 22" height="22" preserveAspectRatio="none"><path d="M0 10 Q130 0 240 10 T390 6 V22 H0Z" fill="var(--teal)"/><path d="M0 16 Q150 6 280 15 T390 13 V22 H0Z" fill="var(--blue)"/></svg>
</div>
<div class="label" style="left:960px;top:391px">Envelope Option 3</div>

</body>
</html>
```